Steadfast Carewell (02)

We're designing a website to sell Medicare Supplements. Attached is the content we want to say and general layout, but please use your best knowledge to make it better. This platform is intentionally simplistic because this is reaching an older demographic, so it should be very straightforward, attention-grabbing and extremely user-friendly, while still appearing reliable and professional.
This should be a two-page web design. The homepage has information on Medicare supplements (script in image attached below) along with a button to input zip code. This triggers a window to pop up asking for personal information (will also be listed in attachment).
This brings you to the second page that lists out the medicare supplement companies and plans based on inputed information. We just want to see the design you have in mind, so it doesn't matter what information you put in this section. Feel free to reference/replicate the information in image 3 in the doc. There should be a section where you can filter results by company, premium price, or coverage plans.
Target Market(s)
Seniors, 65+
Industry/Entity Type
Insurance
Number of Pages Required
2 page
Look and feel

```html
<!DOCTYPE html>
<html lang="en">
<head>
<meta charset="utf-8">
<title>Steadfast Carewell – Medicare Supplement web design</title>
<link rel="stylesheet" href="https://fonts.googleapis.com/css2?family=Lato:ital,wght@0,400;0,700;0,900;1,400&family=Crimson+Text:ital@1&display=swap">
<style>
:root{
  --navy:#1f3b70;
  --navy-deep:#183160;
  --red:#f2405d;
  --ink:#1d1d1f;
  --muted:#6d7482;
  --line:#d6dae2;
  --stage:#eef0f3;
  --white:#ffffff;
  --black:#0e0e10;
}
*{box-sizing:border-box;margin:0;padding:0}
html,body{width:1200px;height:840px;overflow:hidden}
body{background:var(--stage);font-family:'Lato',sans-serif;color:var(--ink);position:relative}
.abs{position:absolute}
.board{position:absolute;overflow:hidden;box-shadow:0 3px 12px rgba(20,30,60,.16)}
.photo{position:absolute}
.serif{font-family:'Crimson Text',serif;font-style:italic}
.red{color:var(--red)}
.navy{color:var(--navy)}

/* ---------- long homepage ---------- */
.home-page{left:36px;top:11px;width:227px;height:817px;background:var(--white)}
.home-page section{position:absolute;left:0;width:227px}
.hp-hero{top:0;height:119px;background:linear-gradient(120deg,#2a4a82,#1d3768 60%,#223f74)}
.hp-brand{left:16px;top:6px;font-size:4px;color:var(--white)}
.hp-nav{right:10px;top:6px;display:flex;gap:5px;font-size:2.6px;color:var(--white)}
.hp-nav .on{color:var(--red)}
.hp-title{left:16px;top:41px;font-size:9.4px;font-weight:900;color:var(--white);letter-spacing:.1px}
.hp-sub{left:16px;top:53px;font-size:4.7px;line-height:5.6px;color:var(--white)}
.pill{border-radius:20px;background:var(--red);color:var(--white);display:flex;align-items:center;justify-content:center}
.hp-read{left:16px;top:71px;width:25px;height:7px;font-size:2px}
.hp-zip{left:16px;top:98px;width:38px;height:13px;background:var(--white);padding:1px 2px}
.hp-zip small{display:block;font-size:2.2px;color:#444}
.hp-zip span{font-size:4px;font-style:italic}
.hp-find{left:54px;top:98px;width:38px;height:13px;background:var(--red);color:var(--white);font-size:4.4px;display:flex;align-items:center;justify-content:center}

.hp-what{top:119px;height:112px;background:var(--white)}
.frame{position:absolute;border:1px solid var(--navy)}
.framed-photo{position:absolute;border:1.5px solid var(--red)}
.hp-h{font-size:8px;font-weight:900;color:var(--navy);line-height:8px}
.hp-h2{font-size:5.3px;font-weight:700;color:var(--red);line-height:7px}
.hp-p{font-size:2.7px;line-height:3.4px}
.hp-list{list-style:none}
.hp-list li{position:relative;padding-left:6px;font-size:2.5px;line-height:3px}
.hp-list li::before{content:"";position:absolute;left:0;top:.3px;width:1.6px;height:1.6px;border-right:.6px solid currentColor;border-bottom:.6px solid currentColor;transform:rotate(-45deg)}

.hp-costs{top:231px;height:113px;background:var(--navy)}
.hp-costs .hp-h{color:var(--white)}
.hp-costs .hp-p,.hp-costs .hp-list{color:var(--white)}
.hp-costs .hp-list b{color:var(--red);font-weight:400}

.hp-products{top:344px;height:260px;background:var(--white)}
.center-h{left:0;width:227px;text-align:center;font-size:8px;color:var(--navy)}
.hp-tabs{left:0;width:227px;top:46px;display:flex;justify-content:center;gap:8px;font-size:2.5px;align-items:center}
.hp-tabs .active{background:var(--navy);color:var(--white);padding:2px 3px;border-radius:10px}
.tile{position:absolute;width:62px;height:52px}
.view-more{left:102px;top:242px;width:25px;height:7px;border-radius:10px;background:var(--navy);color:var(--white);font-size:1.8px;display:flex;align-items:center;justify-content:center}

.hp-reviews{top:604px;height:111px;background:var(--navy)}
.quote-card{position:absolute;border-radius:3px;padding:4px 3px 2px 5px;font-size:2.1px;line-height:2.8px}
.quote-card::before{content:"\201C";position:absolute;left:1.5px;top:-1px;font-size:7px;line-height:7px;font-weight:900}
.quote-card::after{content:"";position:absolute;left:50%;bottom:-2.5px;margin-left:-2.5px;border:2.5px solid transparent;border-bottom:0;border-top-color:inherit}
.qc-grey{background:#e9eaee;color:#555;border-top-color:#e9eaee}
.qc-red{background:var(--red);color:var(--white);border-top-color:var(--red)}
.avatar{position:absolute;width:12px;height:12px;border-radius:50%;background:linear-gradient(#d8d8d8,#9c9c9c);border:1px solid var(--white)}
.rev-name{position:absolute;font-size:2.2px;color:var(--white);width:30px;text-align:center}

.hp-footer{top:715px;height:102px;background:var(--black);color:var(--white)}
.field{position:absolute;height:10px;background:#232327;font-size:2.3px;color:#aaa;padding:3px 2px}
.submit{position:absolute;left:183px;top:40px;width:28px;height:10px;border:.6px solid var(--red);font-size:2.6px;display:flex;align-items:center;justify-content:center}
.foot-col{position:absolute;top:62px;font-size:2.1px;line-height:2.8px;width:48px}
.foot-col b{color:var(--red);font-weight:700}
.social{position:absolute;top:74px;width:6px;height:6px;border-radius:50%;background:#3b5fb0}
.copy{position:absolute;left:0;top:88px;width:227px;border-top:.5px solid #333;padding-top:4px;text-align:center;font-size:2.3px}

/* ---------- hero screen ---------- */
.hero-screen{left:529px;top:42px;width:374px;height:230px;background:linear-gradient(120deg,#2b4c86,#1f3a6c 55%,#26467e)}
.hs-brand{left:3px;top:10px;font-size:8px;color:var(--white)}
.hs-nav{top:11px;font-size:4.8px;color:var(--white)}
.hs-title{left:3px;top:78px;font-size:17.5px;font-weight:900;color:var(--white)}
.hs-sub{left:3px;top:101px;font-size:10.3px;line-height:11px;color:var(--white)}
.hs-read{left:3px;top:137px;width:46px;height:15px;font-size:4.4px}
.hs-zip{left:3px;top:189px;width:72px;height:26px;background:var(--white);padding:3px 4px}
.hs-zip small{display:block;font-size:5px}
.hs-zip span{font-size:8px;font-style:italic}
.hs-find{left:75px;top:189px;width:71px;height:26px;background:var(--red);color:var(--white);font-size:8.4px;display:flex;align-items:center;justify-content:center}

/* ---------- quote modal ---------- */
.quote-board{left:294px;top:353px;width:327px;height:451px;background:#1b2742}
.dim{position:absolute;left:0;width:327px}
.ghost{position:absolute;color:rgba(255,255,255,.16)}
.modal{left:56px;top:90px;width:214px;height:272px;background:var(--white);padding:0 7px}
.modal .t{position:absolute;left:7px}
.m-title{top:10px;font-size:11px}
.m-p{font-size:6.4px;line-height:8.4px;width:200px}
.m-label{font-size:6.6px}
.m-label i{color:var(--red);font-style:normal}
.radio{position:absolute;left:11px;width:7px;height:7px;border:.8px solid var(--navy);border-radius:50%}
.m-input{position:absolute;height:19px;border:1px solid var(--navy);border-radius:2px;font-size:5.2px;color:#999;padding:6px 4px}
.m-btn{position:absolute;left:7px;top:241px;width:60px;height:19px;background:var(--navy);color:var(--white);border-radius:2px;font-size:5.2px;display:flex;align-items:center;gap:3px;padding-left:6px}
.m-cancel{position:absolute;left:72px;top:247px;font-size:5.2px;color:var(--red)}

/* ---------- plans page ---------- */
.plans-board{left:651px;top:354px;width:520px;height:451px;background:var(--white)}
.pl-title{left:37px;top:9px;font-size:13.3px;font-weight:700;color:var(--navy)}
.pl-sort{left:370px;top:14px;font-size:6.6px;color:var(--red)}
.pl-select{left:398px;top:10px;width:83px;height:16px;border:1px solid var(--navy);border-radius:2px;font-size:6.4px;padding:3px 4px;display:flex;justify-content:space-between;align-items:center}
.side-btn{position:absolute;left:37px;width:86px;height:25px;color:var(--white);font-size:7.4px;display:flex;align-items:center;justify-content:center}
.filters{left:37px;top:105px;width:86px;height:342px;border:1px solid var(--line);border-top:0}
.filters-head{height:23px;background:var(--navy);color:var(--white);font-size:7.4px;padding:6px 6px}
.f-group{position:absolute;left:8px;font-size:6.4px;color:var(--red);display:flex;align-items:center;gap:4px}
.f-item{position:absolute;left:6px;font-size:6px;display:flex;align-items:center;gap:3px}
.f-item.off{color:#b5b9c2}
.box{width:8px;height:8px;border:.8px solid currentColor;border-radius:50%;display:inline-flex;align-items:center;justify-content:center}
.f-item .box{border-color:var(--navy)}
.f-item.off .box{border-color:#c9ccd3}
.f-rule{position:absolute;left:3px;width:78px;border-top:1px solid var(--line)}
.plan-card{position:absolute;left:133px;width:349px;height:160px;background:var(--white);box-shadow:0 1px 5px rgba(20,30,60,.15)}
.price-col{position:absolute;left:0;top:0;width:97px;height:100%;background:var(--navy);color:var(--white);text-align:center}
.price{position:absolute;left:0;width:97px;top:30px;font-size:20px;font-weight:700}
.per{position:absolute;left:0;width:97px;top:55px;font-size:8px}
.enroll{position:absolute;left:12px;top:73px;width:73px;height:19px;background:var(--red);border-radius:3px;font-size:8px;display:flex;align-items:center;justify-content:center}
.fav{position:absolute;left:13px;top:136px;font-size:7.2px;display:flex;align-items:center;gap:3px}
.plan-name{position:absolute;left:107px;top:22px;font-size:8.5px;font-weight:400;color:var(--red)}
.hr{position:absolute;left:107px;width:229px;border-top:1px solid var(--navy)}
.cost{position:absolute;top:51px;font-size:11px;font-weight:700;color:var(--navy)}
.cost-l{position:absolute;top:63px;font-size:5.8px}
.vsep{position:absolute;top:45px;height:27px;border-left:1px solid var(--navy)}
.dash{position:absolute;border:1px dashed var(--navy);color:var(--red);font-size:6.6px;display:flex;align-items:center;justify-content:center;border-radius:1px}
.doc-label{position:absolute;left:107px;top:82px;font-size:6.4px}
.feat-label{position:absolute;left:107px;top:102px;font-size:6.2px;color:var(--red)}
.feats{position:absolute;left:160px;top:102px;width:180px;font-size:5.9px;line-height:9.5px}
.feats span{white-space:nowrap;margin-right:4px}
.more{position:absolute;left:107px;top:150px;font-size:6.6px;color:var(--red)}
.compare{position:absolute;left:295px;top:145px;width:43px;height:11px;background:var(--red);color:var(--white);font-size:4.6px;border-radius:1px;display:flex;align-items:center;justify-content:center}
</style>
</head>
<body>

<!-- ===== Homepage, full length ===== -->
<main class="board home-page">
  <section class="hp-hero">
    <div class="abs hp-brand">Steadfast Carewell</div>
    <nav class="abs hp-nav"><span class="on">Home</span><span>About</span><span>Features</span><span>Product</span><span>Reviews</span><span>Faq</span><span>Contact</span></nav>
    <div class="photo" role="img" aria-label="Smiling advisor in shirt and tie holding a tablet" style="left:100px;top:20px;width:110px;height:99px;background:linear-gradient(160deg,rgba(230,236,245,.55),rgba(120,150,200,.35));border-radius:40px 40px 0 0"></div>
    <h1 class="abs hp-title">STEADFAST CAREWELL</h1>
    <p class="abs hp-sub serif">Be confident in choosing the Medicare Supplement<br>plan that's right for you.</p>
    <div class="abs pill hp-read">READ MORE</div>
    <div class="abs hp-zip"><small>Zip Code</small><span>Enter Zip Code</span></div>
    <div class="abs hp-find">Find Plans</div>
  </section>

  <section class="hp-what">
    <div class="frame" style="left:16px;top:9px;width:87px;height:87px"></div>
    <div class="framed-photo" role="img" aria-label="Scientist looking into a microscope" style="left:22px;top:16px;width:88px;height:86px;background:linear-gradient(135deg,#dfe6ee,#9fb3c8)"></div>
    <div class="abs" style="left:115px;top:14px">
      <div class="hp-h">WHAT IS A</div>
      <div class="hp-h2">MEDICARE SUPPLEMENT PLAN?</div>
    </div>
    <p class="abs hp-p" style="left:115px;top:33px;width:95px">Each Medicare Supplement insurance plan offers a different level of basic benefits, but each lettered plan will include the same standardized basic benefits regardless of insurance company and location. Medicare Supplement insurance plans do not always cover vision, dental, long-term care, or hearing aids, but all plans must cover at least a portion of the following basic benefits:</p>
    <ul class="abs hp-list" style="left:115px;top:66px;width:95px">
      <li style="margin-bottom:4px">Medicare Part A coinsurance costs up to an additional 365 days after Medicare benefits are exhausted.</li>
      <li style="margin-bottom:5px">Medicare Part A hospice care coinsurance or copayments.</li>
      <li style="margin-bottom:6px">Medicare Part B coinsurance or copayments.</li>
      <li>First three pints of blood used in a medical procedure.</li>
    </ul>
  </section>

  <section class="hp-costs">
    <div class="abs" style="left:16px;top:13px">
      <div class="hp-h">MEDICARE SUPPLEMENT</div>
      <div class="hp-h2">INSURANCE PLAN COSTS</div>
    </div>
    <p class="abs hp-p" style="left:16px;top:34px;width:98px">Although private insurance companies are required to offer the same basic benefits for each lettered plan, they do have the ability to charge different premiums. You might want to shop around to find a Medicare Supplement insurance plan that may fit your medical and financial needs. Insurance companies may price their plan premiums in any of the following ways:</p>
    <ul class="abs hp-list" style="left:16px;top:66px;width:98px">
      <li style="margin-bottom:5px"><b>Community-no-age-rated:</b> These Medicare Supplement insurance plans charge premiums that are the same across the board, regardless of age.</li>
      <li style="margin-bottom:5px"><b>Issue-age-rated:</b> These plans base their premiums on your age when you first enrolled in the policy. Therefore, the younger you are when.</li>
      <li><b>Attained-age-rated:</b> Like issue-age-rated, these plans base their premiums on the age you were when you first bought a policy.</li>
    </ul>
    <div class="frame" style="left:125px;top:10px;width:86px;height:87px;border-color:var(--white)"></div>
    <div class="framed-photo" role="img" aria-label="Scientist working at a microscope" style="left:118px;top:16px;width:87px;height:87px;background:linear-gradient(135deg,#e4e9ef,#a7b8cb)"></div>
  </section>

  <section class="hp-products">
    <h2 class="abs center-h" style="top:8px"><span class="red">Our</span> Products</h2>
    <p class="abs hp-p" style="left:22px;top:20px;width:183px;text-align:center">Browse plan covers, drug coverage, health extras and supplements. Every option is explained in plain words so you can compare with ease and choose with confidence.</p>
    <div class="abs hp-tabs"><span>MEDICARE COVERS</span><span>DRUG COVERAGE</span><span>HEALTH</span><span class="active">SUPPLEMENTS</span></div>
    <div class="tile" role="img" aria-label="Amber softgel capsules" style="left:16px;top:66px;background:linear-gradient(135deg,#f2c46a,#e9e3d6)"></div>
    <div class="tile" role="img" aria-label="White pill bottles and tablets" style="left:83px;top:66px;background:linear-gradient(135deg,#eef0f1,#c8ccd0)"></div>
    <div class="tile" role="img" aria-label="Assorted pills on a dark surface" style="left:150px;top:66px;background:linear-gradient(135deg,#3a3d42,#7c7f84)"></div>
    <div class="tile" role="img" aria-label="Herbal supplement bottle on yellow" style="left:16px;top:123px;background:linear-gradient(135deg,#f1b93a,#f3efe4)"></div>
    <div class="tile" role="img" aria-label="Rows of capsules on dark blue" style="left:83px;top:123px;background:linear-gradient(135deg,#1f2d4d,#8b94a6)"></div>
    <div class="tile" role="img" aria-label="Orange slices with vitamin tablets" style="left:150px;top:123px;background:linear-gradient(135deg,#f6a43a,#ece6dc)"></div>
    <div class="tile" role="img" aria-label="Blue liquid in test tubes" style="left:16px;top:179px;background:linear-gradient(135deg,#1e8fd6,#a9d8f2)"></div>
    <div class="tile" role="img" aria-label="Medicine bottles with colourful caps" style="left:83px;top:179px;background:linear-gradient(135deg,#e7dfd6,#c9514a)"></div>
    <div class="tile" role="img" aria-label="Green sample tray in a laboratory" style="left:150px;top:179px;background:linear-gradient(135deg,#e9ecef,#2ab58a)"></div>
    <div class="abs view-more">VIEW MORE</div>
  </section>

  <section class="hp-reviews">
    <h2 class="abs center-h" style="top:7px;color:var(--white)">Clients Review</h2>
    <div class="quote-card qc-grey" style="left:16px;top:27px;width:55px;height:42px">Clear plans, kind staff and fair prices. Signing up took ten minutes and now I know my coverage.</div>
    <div class="quote-card qc-red" style="left:81px;top:24px;width:64px;height:48px">They explained every option patiently. I saved money each month and my doctors stayed in network.</div>
    <div class="quote-card qc-grey" style="left:156px;top:27px;width:56px;height:42px">Simple forms, big clear buttons and quick answers on the phone. I recommend them to my friends.</div>
    <div class="avatar" role="img" aria-label="Client portrait" style="left:37px;top:75px"></div>
    <div class="avatar" role="img" aria-label="Client portrait" style="left:107px;top:79px"></div>
    <div class="avatar" role="img" aria-label="Client portrait" style="left:178px;top:75px"></div>
    <div class="rev-name" style="left:28px;top:89px">ADA LANE</div>
    <div class="rev-name" style="left:98px;top:94px;color:var(--red)">ADA LANE</div>
    <div class="rev-name" style="left:169px;top:89px">ADA LANE</div>
  </section>

  <section class="hp-footer">
    <h2 class="abs center-h" style="top:7px;color:var(--white)">Get in <span class="red">Touch</span></h2>
    <div class="field" style="left:16px;top:26px;width:63px">Name</div>
    <div class="field" style="left:82px;top:26px;width:63px">Email</div>
    <div class="field" style="left:148px;top:26px;width:63px">Phone</div>
    <div class="field" style="left:16px;top:40px;width:163px">Message</div>
    <div class="submit">SUBMIT</div>
    <div class="abs" style="left:16px;top:61px;font-size:4.4px">Steadfast Carewell</div>
    <div class="social" style="left:16px"></div><div class="social" style="left:24px;background:#2f8de0"></div><div class="social" style="left:32px;background:#d9453a"></div><div class="social" style="left:40px;background:#e03a78"></div>
    <div class="foot-col" style="left:71px"><b>NEW YORK</b><br>27 Orchard Row, Suite 4,<br>Hillvale 10021<br><br>(800) 555-0142<br>hello@steadfastcarewell.example</div>
    <div class="foot-col" style="left:122px"><b>LONDON</b><br>27 Orchard Row, Suite 4,<br>Hillvale 10021<br><br>(800) 555-0142<br>hello@steadfastcarewell.example</div>
    <div class="foot-col" style="left:173px"><b>MADRID</b><br>27 Orchard Row, Suite 4,<br>Hillvale 10021<br><br>(800) 555-0142<br>hello@steadfastcarewell.example</div>
    <div class="copy">Copyright 2020 steadfastcarewell - All Rights Reserved</div>
  </section>
</main>

<!-- ===== Hero screen ===== -->
<section class="board hero-screen">
  <div class="photo" role="img" aria-label="Smiling advisor in shirt and orange tie holding a tablet with charts" style="left:161px;top:37px;width:213px;height:193px;background:linear-gradient(160deg,rgba(235,240,248,.5),rgba(120,150,200,.3));border-radius:90px 90px 0 0"></div>
  <div class="abs hs-brand">Steadfast Carewell</div>
  <span class="abs hs-nav" style="left:202px;color:var(--red)">Home</span>
  <span class="abs hs-nav" style="left:226px">About</span>
  <span class="abs hs-nav" style="left:250px">Features</span>
  <span class="abs hs-nav" style="left:279px">Product</span>
  <span class="abs hs-nav" style="left:307px">Reviews</span>
  <span class="abs hs-nav" style="left:335px">Faq</span>
  <span class="abs hs-nav" style="left:353px">Contact</span>
  <h1 class="abs hs-title">STEADFAST CAREWELL</h1>
  <p class="abs hs-sub serif">Be confident in choosing the Medicare Supplement<br>plan that's right for you.</p>
  <div class="abs pill hs-read">READ MORE</div>
  <div class="abs hs-zip"><small>Zip Code</small><span>Enter Zip Code</span></div>
  <div class="abs hs-find">Find Plans</div>
</section>

<!-- ===== Quote window over homepage ===== -->
<section class="board quote-board">
  <div class="dim" style="top:0;height:175px;background:#1d2a46"></div>
  <div class="dim" style="top:175px;height:162px;background:#3a3b40"></div>
  <div class="dim" style="top:337px;height:114px;background:#1b2743"></div>
  <div class="ghost" style="left:24px;top:8px;font-size:6px">Steadfast Carewell</div>
  <div class="ghost" style="left:24px;top:58px;font-size:13px;font-weight:900">STEADFAST CAREWELL</div>
  <div class="ghost serif" style="left:24px;top:77px;font-size:7px;line-height:8px">Be confident in choosing the Medicare Supplement<br>plan that's right for you.</div>
  <div class="ghost" style="left:24px;top:142px;width:40px;height:18px;background:rgba(255,255,255,.08);font-size:4px;padding:2px">Zip Code<br>Enter Zip</div>
  <div class="ghost" style="left:24px;top:356px;font-size:11px;font-weight:900">MEDICARE SUPPLEMENT</div>
  <div class="ghost" style="left:24px;top:368px;font-size:8px;font-weight:700;color:rgba(242,64,93,.3)">INSURANCE PLAN COSTS</div>

  <div class="abs modal">
    <h2 class="t m-title"><span class="red">Get a</span> <span class="navy">Quote</span></h2>
    <p class="t m-p" style="top:30px">To figure out what your monthly premium would, be enter your gender and date of birth</p>
    <p class="t m-p" style="top:52px">Contrary to popular belief, Lorem Ipsum is not simply random text. It has roots in a piece of classical Latin literature from 45 BC, making it over 2000 years old.</p>
    <div class="t m-label" style="top:94px"><i>*</i> Required</div>
    <div class="t m-label" style="top:112px"><i>*</i> Gender</div>
    <span class="radio" style="top:125px"></span><div class="t m-label" style="left:22px;top:124px">Male</div>
    <span class="radio" style="top:141px"></span><div class="t m-label" style="left:22px;top:140px">Female</div>
    <div class="t m-label" style="top:159px">Date of birth <i>*</i></div>
    <div class="m-input" style="left:7px;top:170px;width:86px">mm/dd/yyyy</div>
    <div class="t m-label" style="top:197px">Hospital insurance (Part A)</div>
    <div class="t m-label" style="top:208px;font-size:6px">Part A Month <i>*</i></div>
    <div class="t m-label" style="left:98px;top:208px;font-size:6px">Part A Year <i>*</i></div>
    <div class="m-input" style="left:7px;top:217px;width:86px">Date</div>
    <div class="m-input" style="left:98px;top:217px;width:86px">Year</div>
    <div class="m-btn">Compare Rates
      <svg width="5" height="6" viewBox="0 0 5 6"><path d="M1 .5 3.8 3 1 5.5" fill="none" stroke="#fff" stroke-width="1.1"/></svg>
    </div>
    <div class="m-cancel">Cancel</div>
  </div>
</section>

<!-- ===== Plans results page ===== -->
<section class="board plans-board">
  <h2 class="abs pl-title"><span class="red">Medicare</span> Advantage plans</h2>
  <div class="abs pl-sort">Sort by</div>
  <div class="abs pl-select">Monthly Premium
    <svg width="6" height="4" viewBox="0 0 6 4"><path d="M.6.6 3 3 5.4.6" fill="none" stroke="#1d1d1f" stroke-width="1"/></svg>
  </div>

  <div class="side-btn" style="top:42px;background:var(--navy)">+ Add your doctors</div>
  <div class="side-btn" style="top:70px;background:var(--red)">+ Add your Drugs</div>

  <aside class="abs filters">
    <div class="filters-head">Filter Plans by</div>
    <div class="f-group" style="top:28px">&#8964; Company</div>
    <div class="f-item" style="top:43px"><span class="box"><svg width="5" height="4" viewBox="0 0 5 4"><path d="M.5 2 2 3.4 4.5.6" fill="none" stroke="#1f3b70" stroke-width=".9"/></svg></span>All Carriers (3)</div>
    <div class="f-item" style="top:58px"><span class="box"></span>Brightpath Care (3)</div>
    <div class="f-item" style="top:73px"><span class="box"></span>Crestview He ..(3)</div>
    <div class="f-item" style="top:88px"><span class="box"></span>Unionwell Health (3)</div>
    <div class="f-rule" style="top:102px"></div>
    <div class="f-group" style="top:109px">&#8964; Monthly Premium</div>
    <div class="f-item off" style="top:124px"><span class="box"></span>No premium (0)</div>
    <div class="f-item off" style="top:139px"><span class="box"></span>Under $40 (0)</div>
    <div class="f-item" style="top:154px"><span class="box"><svg width="5" height="4" viewBox="0 0 5 4"><path d="M.5 2 2 3.4 4.5.6" fill="none" stroke="#1f3b70" stroke-width=".9"/></svg></span>$50 to $100 (5)</div>
    <div class="f-item off" style="top:169px"><span class="box"></span>$100 to 250 (0)</div>
    <div class="f-item off" style="top:184px"><span class="box"></span>$250 to Above (0)</div>
    <div class="f-rule" style="top:198px"></div>
    <div class="f-group" style="top:204px">&#8964; Plan Type</div>
    <div class="f-item" style="left:18px;top:215px;color:var(--navy)">Help me choose</div>
    <div class="f-item" style="top:228px"><span class="box"></span>HMO (2)</div>
    <div class="f-item off" style="top:243px"><span class="box"></span>HMO POS (0)</div>
    <div class="f-item off" style="top:257px"><span class="box"></span>HMO POS 2 (0)</div>
    <div class="f-item off" style="top:272px"><span class="box"></span>HMO -A (0)</div>
    <div class="f-item off" style="top:287px"><span class="box"></span>HMO -POS (0)</div>
    <div class="f-item off" style="top:301px"><span class="box"></span>HMO A+ (0)</div>
    <div class="f-item off" style="top:316px"><span class="box"></span>HMO B+(0)</div>
  </aside>

  <!-- plan 1 -->
  <article class="plan-card" style="top:43px">
    <div class="price-col">
      <div class="price">$69.0</div><div class="per">Monthly Premium</div>
      <div class="enroll">Enroll Now</div>
      <div class="fav"><svg width="11" height="10" viewBox="0 0 11 10"><path d="M5.5 9.5 1 5A2.7 2.7 0 0 1 5.5 1.4 2.7 2.7 0 0 1 10 5Z" fill="#f2405d"/></svg>Add to Favorites</div>
    </div>
    <h3 class="plan-name">Harborline Advantage (HMO)</h3>
    <div class="hr" style="top:41px"></div>
    <div class="cost" style="left:107px">$10</div><div class="cost-l" style="left:107px">Primary Doctor co-pay</div>
    <div class="vsep" style="left:180px"></div>
    <div class="cost" style="left:186px">$20</div><div class="cost-l" style="left:186px">Speciallist co-pay</div>
    <div class="vsep" style="left:255px"></div>
    <div class="dash" style="left:260px;top:47px;width:65px;height:13px">+ Add Rx Drugs</div><div class="cost-l" style="left:260px">Drug covered</div>
    <div class="hr" style="top:75px"></div>
    <div class="doc-label">Doctor Coverage:</div>
    <div class="dash" style="left:169px;top:80px;width:132px;height:13px">+ Add your doctor to see coverage</div>
    <div class="feat-label">Plan Features:</div>
    <div class="feats"><span>✓ Rx Drugs</span><span>✓ Hospital &amp; medical</span><span>✓ Dental</span><span>✓ Vision</span><br><span>✓ Healing</span><span>✓ Fitness benefits</span><span>✓ Medical healthcare</span><br><span>✓ Over-the-counter benefits</span><span>&nbsp; Mental health care</span><br><span>✓ Chiropractice care</span></div>
    <div class="hr" style="top:142px;left:97px;width:252px"></div>
    <div class="more">view more detail &#8964;</div>
    <div class="compare">Compare</div>
  </article>

  <!-- plan 2 -->
  <article class="plan-card" style="top:212px">
    <div class="price-col">
      <div class="price">$89.0</div><div class="per">Monthly Premium</div>
      <div class="enroll">Enroll Now</div>
      <div class="fav"><svg width="11" height="10" viewBox="0 0 11 10"><path d="M5.5 9.5 1 5A2.7 2.7 0 0 1 5.5 1.4 2.7 2.7 0 0 1 10 5Z" fill="#f2405d"/></svg>Add to Favorites</div>
    </div>
    <h3 class="plan-name">Elderway Medcare Advantage Brightshield (HMO)</h3>
    <div class="hr" style="top:41px"></div>
    <div class="cost" style="left:107px">$15</div><div class="cost-l" style="left:107px">Primary Doctor co-pay</div>
    <div class="vsep" style="left:180px"></div>
    <div class="cost" style="left:186px">$25</div><div class="cost-l" style="left:186px">Speciallist co-pay</div>
    <div class="vsep" style="left:255px"></div>
    <div class="dash" style="left:260px;top:47px;width:65px;height:13px">+ Add Rx Drugs</div><div class="cost-l" style="left:260px">Drug covered</div>
    <div class="hr" style="top:75px"></div>
    <div class="doc-label">Doctor Coverage:</div>
    <div class="dash" style="left:169px;top:80px;width:132px;height:13px">+ Add your doctor to see coverage</div>
    <div class="feat-label">Plan Features:</div>
    <div class="feats"><span>✓ Rx Drugs</span><span>✓ Hospital &amp; medical</span><span>✓ Dental</span><span>✓ Vision</span><br><span>✓ Healing</span><span>✓ Fitness benefits</span><span>✓ Medical healthcare</span><br><span>✓ Chiropractice care</span></div>
    <div class="hr" style="top:142px;left:97px;width:252px"></div>
    <div class="more">view more detail &#8964;</div>
    <div class="compare">Compare</div>
  </article>

  <!-- plan 3 -->
  <article class="plan-card" style="top:380px">
    <div class="price-col">
      <div class="price">$99.0</div><div class="per">Monthly Premium</div>
    </div>
    <h3 class="plan-name">Elderway Medcare (HMO)</h3>
    <div class="hr" style="top:41px"></div>
    <div class="cost" style="left:107px">$25</div><div class="cost-l" style="left:107px">Primary Doctor co-pay</div>
    <div class="vsep" style="left:180px"></div>
    <div class="cost" style="left:186px">$35</div><div class="cost-l" style="left:186px">Speciallist co-pay</div>
    <div class="vsep" style="left:255px"></div>
    <div class="dash" style="left:260px;top:47px;width:65px;height:13px">+ Add Rx Drugs</div><div class="cost-l" style="left:260px">Drug covered</div>
  </article>
</section>

</body>
</html>
```